Flyer-Design für EMS-Training
Zielgruppe
EMS-Training
Aufgabenstellung
Meinen bisherigen Flyer habe ich hochgeladen. Der Text kann sich noch etwas ändern. Beibehalten werden sollen die 'Schwünge' und die Farben grün und lila. Diese gehören zum Corporate Design.
Die Bilder, die eingebaut werden sollen, sind ebenfalls hochgeladen.
Gerne hätte ich auf der Seite mit den Adressdaten eine kleine Karte (am besten illustriert), aus der unser Standort erkennbar ist. Um Platz dafür zu schaffen können die Schlagworte 'Gesundheit, Wohlbefinden, Selbstvertrauen' entfallen. Weiterhin entfernt werden kann der QR-Code.
Hintergrund gerne auch dunkel.

```html
<!DOCTYPE html>
<html lang="de">
<head>
<meta charset="utf-8">
<title>Kraftwelle – EMS-Flyer</title>
<link href="https://fonts.googleapis.com/css2?family=Montserrat:wght@400;600;700;800&family=Raleway:wght@300;400;500&display=swap" rel="stylesheet">
<style>
:root{
  --page:#efefef;
  --ink:#2b2a2b;
  --ink-deep:#222122;
  --lime:#c9d400;
  --purple:#8b2e98;
  --white:#ffffff;
  --soft:#d9d9d9;
  --rule:#8f9400;
}
*{box-sizing:border-box;margin:0;padding:0}
html,body{width:1200px;height:2461px;overflow:hidden;background:var(--page)}
body{position:relative;font-family:"Raleway",sans-serif;color:var(--white)}
.spread{position:absolute;left:50px;width:1100px;height:778px;background:var(--ink);box-shadow:0 18px 40px rgba(0,0,0,.18);overflow:hidden}
.spread-inside{top:392px}
.spread-outside{top:1290px}
.swoosh{position:absolute;inset:0;width:100%;height:100%;pointer-events:none}
.panel{position:absolute;top:0;width:366.67px;height:778px}
.p1{left:0}.p2{left:366.67px}.p3{left:733.33px}
.fold{position:absolute;top:0;width:1px;height:100%;background:rgba(0,0,0,.25)}
.photo{position:absolute}
.headline{font-family:"Montserrat",sans-serif;font-weight:800;color:var(--lime);font-size:22px;line-height:1;text-transform:uppercase}
.subline{font-family:"Montserrat",sans-serif;font-weight:400;font-size:15px;text-transform:uppercase;color:var(--white);margin-top:3px}
.pulse{display:block;margin-top:4px}
.body-copy{font-size:11.5px;line-height:1.45;font-weight:300;color:var(--soft)}
.body-copy p{margin-bottom:7px}
.benefit-list{position:absolute;list-style:none}
.benefit-list li{display:flex;align-items:center;gap:14px;height:52px}
.benefit-list .label{font-family:"Montserrat",sans-serif;font-weight:700;font-size:13px;text-transform:uppercase;line-height:1.15;border-bottom:1px solid var(--lime);padding-bottom:4px;flex:1}
.icon{flex:none;width:30px;height:30px}
.goal-list{position:absolute;list-style:none}
.goal-list li{display:flex;gap:8px;align-items:flex-start;font-size:11px;line-height:1.3;color:var(--soft);border-bottom:1px solid var(--rule);padding:7px 0 6px}
.goal-list svg{flex:none;margin-top:1px}
.cta-text{font-size:13px;line-height:1.3;color:var(--white);text-align:center}
.cta-strong{font-family:"Montserrat",sans-serif;font-weight:800;font-size:19px;text-align:center;margin-top:4px}
.bar{position:absolute;display:flex;align-items:center;height:30px;background:var(--lime);color:var(--ink-deep);font-family:"Montserrat",sans-serif;font-weight:700;font-size:14px;padding-left:30px;white-space:nowrap}
.bar-web{font-family:"Raleway",sans-serif;font-weight:500;font-size:12px}
.bar-badge{position:absolute;left:-14px;top:-2px;width:34px;height:34px;border-radius:50%;background:var(--white);display:flex;align-items:center;justify-content:center}
.vertical-tag{position:absolute;transform:rotate(-90deg);transform-origin:left top;font-family:"Montserrat",sans-serif;font-weight:700;font-size:10px;letter-spacing:.5px;white-space:nowrap}
.vertical-tag b{color:var(--lime)}
.timer{position:absolute;width:70px;height:70px;border:2px solid var(--white);border-radius:50%;display:flex;flex-direction:column;align-items:center;justify-content:center;font-family:"Montserrat",sans-serif;font-size:10px;line-height:1.1;text-align:center;background:var(--ink)}
.timer b{color:var(--lime);font-size:14px;font-weight:800}
.timer::before{content:"";position:absolute;top:-9px;left:27px;width:12px;height:6px;border:2px solid var(--white);border-radius:2px}
.brand-name{font-family:"Montserrat",sans-serif;font-weight:700;font-size:28px;color:var(--lime);letter-spacing:1px;display:flex;align-items:center;gap:8px}
.brand-dot{width:16px;height:16px;border-radius:50%;background:var(--purple)}
.brand-tag{font-size:11px;color:var(--purple);font-weight:500;margin-top:2px;text-align:right}
.contact-list{position:absolute;list-style:none}
.contact-list li{display:flex;gap:14px;align-items:center;font-size:10.5px;line-height:1.3;color:var(--soft);border-bottom:1px solid var(--rule);padding:9px 0}
.contact-list strong{color:var(--white);font-family:"Montserrat",sans-serif;font-size:10px}
.visit{position:absolute;text-align:center;font-family:"Montserrat",sans-serif;text-transform:uppercase}
.visit span{display:block;font-size:14px;font-weight:400}
.visit strong{display:block;font-size:18px;font-weight:800;color:var(--lime)}
.url{position:absolute;font-family:"Montserrat",sans-serif;font-weight:700;font-size:15px;text-align:center;width:100%}
.perk-list{position:absolute;list-style:none}
.perk-list li{display:flex;gap:14px;align-items:center;height:60px;border-bottom:1px solid var(--rule)}
.perk-list h3{font-family:"Montserrat",sans-serif;font-weight:700;font-size:11.5px;text-transform:uppercase;color:var(--white)}
.perk-list p{font-size:10px;color:var(--soft);line-height:1.3;margin-top:2px}
.claim-box{position:absolute;border:1.5px solid var(--lime);border-radius:14px;font-family:"Montserrat",sans-serif;font-size:12.5px;text-transform:uppercase;text-align:center;line-height:1.3;padding:14px 10px}
.claim-box b{font-weight:700}
.cover-head{position:absolute;width:100%;text-align:center;font-family:"Montserrat",sans-serif}
.cover-head .big{font-weight:800;font-size:32px;color:var(--lime);text-transform:uppercase}
.cover-head .small{font-weight:700;font-size:19px;text-transform:uppercase}
.cover-head .web{font-weight:700;font-size:15px;margin-top:12px;display:block}
.seal{position:absolute;width:76px;height:76px;border-radius:50%;background:var(--white);border:3px solid var(--ink-deep);box-shadow:0 0 0 2px var(--white)}
</style>
</head>
<body>

<section class="spread spread-inside" aria-label="Flyer Innenseite">
  <div class="photo" role="img" aria-label="Foto: Frau im EMS-Anzug beim Bauchtraining auf einer Matte" style="left:0;top:530px;width:560px;height:248px;background:linear-gradient(160deg,#3a393a 0%,#5c5b5d 55%,#2e2d2e 100%)"></div>
  <div class="photo" role="img" aria-label="Foto: Frau im EMS-Anzug mit Kurzhanteln über dem Kopf" style="left:366.67px;top:0;width:366.67px;height:210px;background:linear-gradient(180deg,#f4f4f4,#d8d8d8)"></div>
  <div class="photo" role="img" aria-label="Foto: Frau im EMS-Anzug in der Hocke mit Kettlebell" style="left:733.33px;top:440px;width:130px;height:338px;background:linear-gradient(180deg,#3b3a3c,#4d4c4e 60%,#2b2a2b)"></div>

  <svg class="swoosh" viewBox="0 0 1100 778" aria-hidden="true">
    <path d="M0 468 C120 440 260 425 400 422 L400 436 C260 440 120 458 0 488 Z" fill="var(--purple)"/>
    <path d="M0 500 C130 470 270 455 400 452 L400 462 C270 466 130 484 0 514 Z" fill="var(--purple)"/>
    <path d="M410 290 C460 230 560 200 733 194 L733 208 C580 214 495 244 426 300 Z" fill="var(--lime)"/>
    <path d="M400 330 C450 270 560 234 733 228 L733 236 C570 244 470 278 410 336 Z" fill="var(--lime)"/>
  </svg>

  <div class="panel p1">
    <div style="position:absolute;left:30px;top:36px;width:310px">
      <h2 class="headline">Bewegung ist wichtig</h2>
      <div class="subline">Für Körper, Geist &amp; Seele</div>
      <svg class="pulse" width="300" height="14" viewBox="0 0 300 14"><polyline points="0,10 250,10 256,2 262,13 268,10 300,10" fill="none" stroke="var(--lime)" stroke-width="1.2"/></svg>
      <div class="body-copy" style="margin-top:12px">
        <p>Zu wenig Bewegung lässt unsere Muskeln verkümmern, führt zu Übergewicht und den heute sehr verbreiteten Wohlstandskrankheiten.</p>
        <p>Rückenschmerzen, Herzkrankheiten, Diabetes oder auch Osteoporose sind nur einige Krankheiten, die durch Bewegungsmangel begünstigt werden.</p>
        <p>Ein effektives Muskeltraining in Kombination mit der richtigen Ernährung kann diesen Teufelskreis durchbrechen.</p>
        <p>Sie stärken mit dem Training z.B. die so wichtige Haltemuskulatur im Rücken, erhöhen Ihren täglichen Kalorienverbrauch und steigern Ihre Leistungsfähigkeit im Alltag und im Beruf.</p>
        <p>Ganz nebenbei profitieren Sie zudem von den nicht zu übersehenden optischen Effekten.</p>
      </div>
    </div>
  </div>
  <div class="fold" style="left:366.67px"></div>

  <div class="panel p2">
    <div class="timer" style="left:250px;top:250px"><span>IN NUR</span><b>20MIN</b></div>
    <div class="vertical-tag" style="left:38px;top:540px">IN NUR <b>20 MINUTEN</b> TRAINING</div>
    <div style="position:absolute;left:60px;top:350px;width:1px;height:190px;background:var(--lime)"></div>
    <ul class="benefit-list" style="left:76px;top:340px;width:270px">
      <li><svg class="icon" viewBox="0 0 30 30"><circle cx="15" cy="15" r="14" fill="none" stroke="var(--white)" stroke-width="1.3"/><path d="M15 7v16M11 10h8M11 15h8M11 20h8" stroke="var(--white)" stroke-width="1.3"/></svg><span class="label">Starker Rücken,<br>keine Schmerzen</span></li>
      <li><svg class="icon" viewBox="0 0 30 30"><circle cx="15" cy="15" r="14" fill="none" stroke="var(--white)" stroke-width="1.3"/><path d="M8 20c3-8 6-11 9-9s2 5-2 6M17 11l4-3" fill="none" stroke="var(--white)" stroke-width="1.3"/></svg><span class="label">Trainierte Muskeln</span></li>
      <li><svg class="icon" viewBox="0 0 30 30"><circle cx="15" cy="15" r="14" fill="none" stroke="var(--white)" stroke-width="1.3"/><rect x="9" y="9" width="12" height="12" rx="2" fill="none" stroke="var(--white)" stroke-width="1.3"/><path d="M12 13h6" stroke="var(--white)" stroke-width="1.3"/></svg><span class="label">Weniger Gewicht</span></li>
      <li><svg class="icon" viewBox="0 0 30 30"><circle cx="15" cy="15" r="14" fill="none" stroke="var(--white)" stroke-width="1.3"/><path d="M10 8c2 5 2 9 0 14M20 8c-2 5-2 9 0 14" fill="none" stroke="var(--white)" stroke-width="1.3"/></svg><span class="label">Straffe Haut</span></li>
    </ul>
  </div>
  <div class="fold" style="left:733.33px"></div>

  <div class="panel p3">
    <div style="position:absolute;left:30px;top:36px;width:310px">
      <h2 class="headline">Trainingsziele</h2>
      <div class="subline">Bei Kraftwelle</div>
      <svg class="pulse" width="300" height="14" viewBox="0 0 300 14"><polyline points="0,10 160,10 166,2 172,13 178,10 300,10" fill="none" stroke="var(--lime)" stroke-width="1.2"/></svg>
    </div>
    <ul class="goal-list" style="left:30px;top:100px;width:310px">
      <li><svg width="13" height="13" viewBox="0 0 13 13"><circle cx="6.5" cy="6.5" r="5.8" fill="none" stroke="var(--lime)"/><path d="M3.5 6.5l2 2 4-4" fill="none" stroke="var(--lime)" stroke-width="1.3"/></svg>Aufbau und Erhalt der Muskulatur</li>
      <li><svg width="13" height="13" viewBox="0 0 13 13"><circle cx="6.5" cy="6.5" r="5.8" fill="none" stroke="var(--lime)"/><path d="M3.5 6.5l2 2 4-4" fill="none" stroke="var(--lime)" stroke-width="1.3"/></svg>Stabilisierung des Halteapparates durch Kräftigung der Haltemuskeln</li>
      <li><svg width="13" height="13" viewBox="0 0 13 13"><circle cx="6.5" cy="6.5" r="5.8" fill="none" stroke="var(--lime)"/><path d="M3.5 6.5l2 2 4-4" fill="none" stroke="var(--lime)" stroke-width="1.3"/></svg>Kräftigung der tiefen Muskelschichten, die herkömmliches Training nur schwer erreicht</li>
      <li><svg width="13" height="13" viewBox="0 0 13 13"><circle cx="6.5" cy="6.5" r="5.8" fill="none" stroke="var(--lime)"/><path d="M3.5 6.5l2 2 4-4" fill="none" stroke="var(--lime)" stroke-width="1.3"/></svg>Linderung von Rücken- und Gelenkproblemen</li>
      <li><svg width="13" height="13" viewBox="0 0 13 13"><circle cx="6.5" cy="6.5" r="5.8" fill="none" stroke="var(--lime)"/><path d="M3.5 6.5l2 2 4-4" fill="none" stroke="var(--lime)" stroke-width="1.3"/></svg>Training der Ausdauer und des Herz-Kreislauf-Systems</li>
      <li><svg width="13" height="13" viewBox="0 0 13 13"><circle cx="6.5" cy="6.5" r="5.8" fill="none" stroke="var(--lime)"/><path d="M3.5 6.5l2 2 4-4" fill="none" stroke="var(--lime)" stroke-width="1.3"/></svg>Stoffwechsel-Training – Anregen der Fettverbrennung und Gewichtsreduktion</li>
      <li><svg width="13" height="13" viewBox="0 0 13 13"><circle cx="6.5" cy="6.5" r="5.8" fill="none" stroke="var(--lime)"/><path d="M3.5 6.5l2 2 4-4" fill="none" stroke="var(--lime)" stroke-width="1.3"/></svg>Straffung der Haut und damit verbunden der Abbau von Cellulite</li>
    </ul>
    <svg style="position:absolute;left:140px;top:440px" width="200" height="14" viewBox="0 0 200 14"><polyline points="0,10 140,10 146,2 152,13 158,10 200,10" fill="none" stroke="var(--lime)" stroke-width="1.2"/></svg>
    <div style="position:absolute;left:142px;top:464px;width:206px">
      <p class="cta-text">Legen Sie noch heute den Grundstein für eine gesunde Zukunft. Vereinbaren Sie jetzt Ihr kostenloses</p>
      <p class="cta-strong">PROBETRAINING!</p>
    </div>
    <div class="bar" style="left:160px;top:585px;width:186px">
      <span class="bar-badge"><svg width="18" height="18" viewBox="0 0 18 18"><path d="M4 2l3 3-2 2c1 2 3 4 5 5l2-2 3 3-2 3C8 15 3 10 2 4z" fill="var(--purple)"/></svg></span>0561 / 48 27 19 30
    </div>
    <div class="bar bar-web" style="left:160px;top:635px;width:186px">
      <span class="bar-badge"><svg width="18" height="18" viewBox="0 0 18 18"><circle cx="9" cy="9" r="7" fill="none" stroke="var(--purple)" stroke-width="1.6"/><path d="M2 9h14M9 2c-3 4-3 10 0 14M9 2c3 4 3 10 0 14" fill="none" stroke="var(--purple)" stroke-width="1.3"/></svg></span>www.kraftwelle-ems.de
    </div>
  </div>
</section>

<section class="spread spread-outside" aria-label="Flyer Außenseite">
  <div class="photo" role="img" aria-label="Foto: Frau im EMS-Anzug mit Kettlebell vor einer Betonwand" style="left:780px;top:150px;width:300px;height:330px;border-radius:0 0 0 150px;background:linear-gradient(135deg,#b9b6b0,#8d8a85 60%,#5d5b58)"></div>
  <svg class="swoosh" viewBox="0 0 1100 778" aria-hidden="true">
    <path d="M733 250 C770 180 880 150 1100 145 L1100 160 C900 166 790 196 748 262 Z" fill="var(--purple)"/>
    <path d="M760 500 C900 490 1040 430 1100 330 L1100 370 C1040 460 910 515 770 520 Z" fill="var(--lime)"/>
    <path d="M748 530 C920 525 1060 470 1100 410 L1100 420 C1060 485 930 540 752 542 Z" fill="var(--lime)"/>
  </svg>

  <div class="panel p1">
    <div style="position:absolute;left:30px;top:40px;width:310px">
      <h2 class="headline">Vorteile</h2>
      <div class="subline">Bei Kraftwelle</div>
      <svg class="pulse" width="300" height="14" viewBox="0 0 300 14"><polyline points="0,10 160,10 166,2 172,13 178,10 300,10" fill="none" stroke="var(--lime)" stroke-width="1.2"/></svg>
    </div>
    <ul class="perk-list" style="left:30px;top:118px;width:310px">
      <li><svg class="icon" viewBox="0 0 30 30"><circle cx="15" cy="15" r="14" fill="none" stroke="var(--lime)" stroke-width="1.3"/><circle cx="15" cy="15" r="7" fill="none" stroke="var(--white)" stroke-width="1.3"/><circle cx="15" cy="15" r="2" fill="var(--white)"/></svg><div><h3>Persönliche Betreuung</h3><p>unsere Trainer helfen Ihnen, Ihr persönliches Ziel zu erreichen.</p></div></li>
      <li><svg class="icon" viewBox="0 0 30 30"><circle cx="15" cy="15" r="14" fill="none" stroke="var(--lime)" stroke-width="1.3"/><rect x="10" y="8" width="10" height="14" rx="1" fill="none" stroke="var(--white)" stroke-width="1.3"/><path d="M12 12h6M12 15h6M12 18h4" stroke="var(--white)"/></svg><div><h3>Individuelle Trainingsplanung</h3><p>für die Erreichung Ihres persönlichen Trainingsziels.</p></div></li>
      <li><svg class="icon" viewBox="0 0 30 30"><circle cx="15" cy="15" r="14" fill="none" stroke="var(--lime)" stroke-width="1.3"/><circle cx="15" cy="17" r="5" fill="none" stroke="var(--white)" stroke-width="1.3"/><path d="M12 12c0-3 6-3 6 0" fill="none" stroke="var(--white)" stroke-width="1.3"/></svg><div><h3>Effektives Training</h3><p>durch Nutzung einer zukunftsweisenden EMS-Technologie.</p></div></li>
      <li><svg class="icon" viewBox="0 0 30 30"><circle cx="15" cy="15" r="14" fill="none" stroke="var(--lime)" stroke-width="1.3"/><circle cx="15" cy="16" r="7" fill="none" stroke="var(--white)" stroke-width="1.3"/><path d="M15 12v4l3 2M13 7h4" fill="none" stroke="var(--white)" stroke-width="1.3"/></svg><div><h3>Hohe Zeitersparnis</h3><p>20 Minuten pro Woche genügen.</p></div></li>
      <li><svg class="icon" viewBox="0 0 30 30"><circle cx="15" cy="15" r="14" fill="none" stroke="var(--lime)" stroke-width="1.3"/><circle cx="15" cy="15" r="8" fill="none" stroke="var(--white)" stroke-width="1.3"/><path d="M11 17c2 3 6 3 8 0" fill="none" stroke="var(--white)" stroke-width="1.3"/></svg><div><h3>Angenehme Atmosphäre</h3><p>man muss es erlebt haben, um es zu spüren.</p></div></li>
      <li><svg class="icon" viewBox="0 0 30 30"><circle cx="15" cy="15" r="14" fill="none" stroke="var(--lime)" stroke-width="1.3"/><circle cx="15" cy="17" r="6" fill="none" stroke="var(--white)" stroke-width="1.3"/><path d="M15 11c0-2 2-3 3-3" fill="none" stroke="var(--white)" stroke-width="1.3"/></svg><div><h3>Ernährungsberatung</h3><p>von Experten begleitet, um Ihr Trainingsziel zu erreichen.</p></div></li>
    </ul>
    <div class="claim-box" style="left:40px;top:640px;width:290px">Unser Trainingsgerät ist <b>medizinisch zugelassen</b> und wurde in <b>Deutschland entwickelt &amp; hergestellt</b></div>
  </div>
  <div class="fold" style="left:366.67px"></div>

  <div class="panel p2">
    <div style="position:absolute;left:60px;top:44px">
      <div class="brand-name"><span class="brand-dot"></span>KRAFTWELLE</div>
      <div class="brand-tag">Stark in jeder Minute</div>
    </div>
    <ul class="contact-list" style="left:30px;top:130px;width:306px">
      <li><svg class="icon" viewBox="0 0 30 30"><circle cx="15" cy="15" r="14" fill="none" stroke="var(--lime)" stroke-width="1.3"/><circle cx="15" cy="12" r="4" fill="none" stroke="var(--white)" stroke-width="1.3"/><path d="M8 22c1-5 13-5 14 0" fill="none" stroke="var(--white)" stroke-width="1.3"/></svg><span><strong>KRAFTWELLE</strong><br>Jonas Berthold</span></li>
      <li><svg class="icon" viewBox="0 0 30 30"><circle cx="15" cy="15" r="14" fill="none" stroke="var(--lime)" stroke-width="1.3"/><path d="M15 23c-4-5-6-8-6-11a6 6 0 0 1 12 0c0 3-2 6-6 11z" fill="none" stroke="var(--white)" stroke-width="1.3"/><circle cx="15" cy="12" r="2" fill="var(--white)"/></svg><span>Am Lindenhof 7<br>34117 Kassel</span></li>
      <li><svg class="icon" viewBox="0 0 30 30"><circle cx="15" cy="15" r="14" fill="none" stroke="var(--lime)" stroke-width="1.3"/><path d="M10 8l3 3-2 2c1 2 3 4 5 5l2-2 3 3-2 3c-6-1-10-5-11-11z" fill="none" stroke="var(--white)" stroke-width="1.3"/></svg><span>Telefonnummer:<br>0561 / 48 27 19 30</span></li>
      <li><svg class="icon" viewBox="0 0 30 30"><circle cx="15" cy="15" r="14" fill="none" stroke="var(--lime)" stroke-width="1.3"/><rect x="8" y="10" width="14" height="10" fill="none" stroke="var(--white)" stroke-width="1.3"/><path d="M8 10l7 6 7-6" fill="none" stroke="var(--white)" stroke-width="1.3"/></svg><span>service@kraftwelle-ems.de<br>www.kraftwelle-ems.de</span></li>
    </ul>
    <div class="visit" style="left:0;width:100%;top:388px"><span>Wir freuen uns auf</span><strong>Ihren Besuch!</strong></div>
    <div style="position:absolute;left:40px;top:450px;width:286px;height:205px;border:1.5px solid var(--lime);border-radius:16px;padding:10px">
      <div role="img" aria-label="Illustrierte Stadtkarte mit markiertem Standort des Studios" style="width:100%;height:100%;border-radius:10px;background:linear-gradient(135deg,#3a393a,#454446)"></div>
    </div>
    <div style="position:absolute;left:30px;top:690px;width:306px;height:1px;background:var(--lime)"></div>
    <div class="url" style="top:705px">www.kraftwelle-ems.de</div>
  </div>
  <div class="fold" style="left:733.33px"></div>

  <div class="panel p3">
    <div style="position:absolute;left:60px;top:40px">
      <div class="brand-name"><span class="brand-dot"></span>KRAFTWELLE</div>
      <div class="brand-tag">Stark in jeder Minute</div>
    </div>
    <div class="seal" role="img" aria-label="Siegel" style="left:250px;top:405px"></div>
    <div class="cover-head" style="top:580px">
      <div class="big">In 20 Minuten</div>
      <div class="small">zum Trainingserfolg</div>
      <span class="web">www.kraftwelle-ems.de</span>
    </div>
    <div style="position:absolute;left:30px;top:700px;width:306px;height:1px;background:var(--lime)"></div>
  </div>
</section>

</body>
</html>
```